Harwood Cleaning – Website Redesign (Clean, Modern, Trust-Focused)

Harwood Cleaning — Homepage Redesign Brief

Project Goal

We need a complete redesign of the homepage for our cleaning business, Harwood Cleaning.
The goal is a clean, modern, trust-building homepage that works equally well for:
• Residential clients
• Commercial clients

The page should feel polished, reliable, easy to navigate, and completely free from clutter, gimmicks, or corporate-sounding fluff.

About Us (Context)

Harwood Cleaning has operated in Sale, Victoria for over 30 years.
Our brand is built on:
• Reliability
• Convenience
• Long-term trust
• Straightforward, no-nonsense communication

We do not want to look like a large franchise, and we do not want to look cute or playful.
The design must feel modern, practical, confident, and professional.

What We Need Designed — Homepage Only

1. Hero Section

A clean, modern hero area with:
• A simple image or clean background (no clutter, no heavy overlays).
Images from our current site may be helpful, or you may source alternatives.
• Headline suggestion (designer may refine):
“30+ Years of Commercial and Residential Cleaning in Sale”
• Sub-headline suggestion:
“Trusted by locals for three decades.”
• Primary CTA button: Get a Quote

2. Trust-Building Logos

Positioned directly beneath the hero:
• Small, neat logos of organisations we work with
(RTB, Brightway, Eastvale District Health, KPL, etc.)
• A clean Rateline Reviews block (stars + review count)
• Must be compact, tidy, evenly spaced — not loud or oversized

3. Trust Block / Problem–Solution Copy

This section introduces why hiring cleaners can be stressful and why reliability matters.

Headline example:
“Call the cleaners you can count on.”

We have existing copy for this section.
Please present it in a minimal, breathable, modern layout that is easy to scan.

4. Stats / Counters Section

Three sharp, structured stat boxes:
• 92+ Recurring Clients
• 4,150+ Visits Per Year
• 265+ Pre-Sale / Exit Cleans

These should look clean and understated — not oversized or gimmicky.

5. Values Section

A short section featuring our core values:
• Be Real
• Do It Right
• Have Fun
• Make It Easy

Designer has flexibility with layout.
(Sections 5 and 6 may swap depending on what flows better.)

6. Services Preview

A simple grid or row with links to our main services:
• Commercial Cleaning
• Residential Cleaning
• Window Cleaning
• Steam Cleaning

Small icons or photos are fine — but no clip art or cartoon-style graphics.

7. Footer

A very clean, simple footer with contact details.
No clutter, no heavy visual styling.

Style Requirements

Overall Tone
• Clean
• Modern
• Minimal
• Trust-driven
• Easy to read and navigate

Do NOT use
• Clip art
• Cute or playful icons
• Flowers, sparkles, “feminine” cleaning imagery
• Heavy or overly bold corporate fonts
• Busy backgrounds
• Long paragraphs of text

Reference Material

Current Website (for copy + structure only)

https://harwoodcleaning.example.au

Rough Sketchly Mock-Up (layout inspiration only)

(We will upload this separately. It’s not a final design — just a loose concept for spacing/flow.)

Logo

Please use the new Harwood Cleaning logo (uploaded in files) or a placeholder if needed. Attached is a potential for a new logo or site colours not wedded to the idea though.

What the Homepage Should Communicate

Within seconds, a visitor should understand that:
• We are established
• We are local
• We are reliable
• We make cleaning easy
• Getting a quote is quick and simple

The homepage should feel effortless, trustworthy, and modern.

Deliverable

A complete homepage design layout suitable for WordPress.
Figma, Adobe XD, or a similar design tool is fine.

Target Market(s)

Residential and commercial clients in Sale, Victoria and surrounding Gippsland region. Typical clients include busy households, office managers, receptionists, medical centres, community organisations, local businesses, and real estate/property professionals. Clients value reliability, simplicity, and stress-free long-term cleaning support.

Industry/Entity Type

Cleaning services (Residential & Commercial)

Font styles to use
Sans Serif

Requirements
Must have
• • Clean, modern, minimal layout • A trust-driven design that highlights proof (logos, stats, reviews) near the top • Clear hierarchy and no clutter • A strong hero section with simple messaging and a clear CTA • Trust logos + Rateline Reviews block directly under the hero • Structured stats/counters section • Values section (Be Real, Do It Right, Have Fun, Make It Easy) • Services preview (Commercial, Residential, Window, Steam/Carpet) • Clean footer with contact details • Use our new Harwood Cleaning logo (or placeholder if needed) • Easy-to-read typography and spacing • Must feel like a local, real cleaning business — not a franchise
Nice to have
• • An option with centred hero text and an option with left-aligned text • Option to preview hero section with or without a quote form • Subtle use of the navy + gold palette (not heavy or corporate) • Soft, minimal background images (not busy city skylines) • Subtle section dividers or whitespace breaks to improve flow • Slightly rounded card corners for a friendly but still modern feel
Should not have
• • No clip-art, cartoon mops, sparkles, bubbles, or generic cleaning icons • No overly bold, blocky, or corporate fonts • No “mega-city” skylines (we are a regional/rural business) • No heavy overlays, dark gradients, or cluttered hero images • No long paragraphs or dense text blocks • No template-style designs that look generic or AI-generated • No overly feminine, overly masculine, or overly playful designs • No neon colors or high-saturation palettes

```html
<!DOCTYPE html>
<html lang="en">
<head>
<meta charset="utf-8">
<title>Harwood Cleaning – Home</title>
<link href="https://fonts.googleapis.com/css2?family=Poppins:wght@400;500;600;700&display=swap" rel="stylesheet">
<style>
:root{
  --navy:#13294b;
  --gold:#7a5f22;
  --sky:#8db3ee;
  --ink:#1a1a1a;
  --muted:#444;
  --partner:#4a4f5a;
  --partner-mark:#c9ccd2;
  --band:#f0f0f0;
  --white:#fff;
  --star:#e2622b;
}
*{box-sizing:border-box;margin:0;padding:0}
html,body{width:1200px;height:4181px;overflow:hidden}
body{font-family:'Poppins',sans-serif;color:var(--ink);background:var(--white);position:relative}
.abs{position:absolute}
.wordmark{display:flex;align-items:center;gap:12px;font-weight:600;font-size:26px;color:var(--white);white-space:nowrap}
.wordmark-mark{width:14px;height:14px;border-radius:50%;background:currentColor;flex:none}

/* hero */
.hero{left:0;top:0;width:1200px;height:747px;background:linear-gradient(120deg,#1c3563 0%,#1a3360 45%,#233d6c 70%,#15294f 100%)}
.nav{top:62px;left:470px;display:flex;gap:26px;font-size:13px;font-weight:600;color:var(--white)}
.nav .active{color:#c9a23c}
.call{left:868px;top:48px;display:flex;align-items:center;gap:14px;color:var(--white)}
.call-icon{width:48px;height:48px;border-radius:50%;background:var(--gold);display:flex;align-items:center;justify-content:center}
.call small{display:block;font-size:11px;font-weight:500}
.call strong{display:block;font-size:19px;font-weight:600}
.hero-title{top:252px;left:0;width:1200px;text-align:center;color:var(--white);font-size:37px;font-weight:600;line-height:52px;text-transform:uppercase}
.hero-title span{color:var(--sky)}
.hero-sub{top:389px;left:0;width:1200px;text-align:center;color:var(--white);font-size:22px;font-weight:600}
.btn{display:flex;align-items:center;justify-content:center;color:var(--white);font-weight:600;font-size:14px}
.btn-gold{background:var(--gold);left:526px;top:450px;width:148px;height:42px}

/* trust */
.trust{left:0;top:747px;width:1200px;height:228px;background:var(--band)}
.partner{display:flex;align-items:center;gap:12px;font-weight:600;color:var(--partner);font-size:18px;top:96px}
.partner-mark{width:32px;height:32px;border-radius:4px;background:var(--partner-mark);flex:none}
.reviews{left:878px;top:77px}
.reviews .row{display:flex;align-items:center;gap:10px;font-size:19px}
.reviews .count{font-size:17px;font-weight:500;margin-top:6px}

/* services */
.section-title{left:0;width:1200px;text-align:center;font-size:34px;font-weight:600;color:#111;text-transform:uppercase}
.section-title span{color:var(--navy)}
.photo{position:absolute;width:422px;height:262px}
.svc-icon{position:absolute;width:70px;height:70px;border-radius:50%;background:var(--navy);border:3px solid var(--white);display:flex;align-items:center;justify-content:center}
.svc-text{position:absolute;width:422px;padding:0 17px}
.svc-text h3{font-size:19px;font-weight:600;margin-bottom:12px}
.svc-text p{font-size:13px;line-height:25px;color:var(--muted)}
.card-raised{position:absolute;left:609px;top:1600px;width:422px;height:148px;background:var(--white);border-radius:8px;box-shadow:0 8px 40px rgba(0,0,0,.08)}

/* gold band */
.cta{left:0;top:2132px;width:1200px;height:544px;background:linear-gradient(100deg,#6c5622,#75602a 50%,#6a5522)}
.cta h2{position:absolute;top:132px;width:1200px;text-align:center;color:var(--white);font-size:34px;font-weight:600}
.cta h4{position:absolute;top:215px;width:1200px;text-align:center;color:var(--white);font-size:15px;font-weight:600}
.cta p{position:absolute;top:268px;width:1200px;text-align:center;color:var(--white);font-size:13px;line-height:26px}
.btn-navy{background:var(--navy);left:526px;top:388px;width:148px;height:43px}

/* values */
.ring{left:413px;top:2899px;width:374px;height:374px;border-radius:50%;border:2px solid #dfe4f0}
.ring-inner{left:445px;top:2931px;width:310px;height:310px;border-radius:50%;background:var(--white);box-shadow:0 0 40px rgba(19,41,75,.08)}
.dot{width:26px;height:26px;border-radius:50%;background:var(--gold);border:3px solid var(--white)}
.value h3{font-size:19px;font-weight:600;margin-bottom:10px}
.value p{font-size:13px;line-height:25px;color:var(--muted)}
.value.left{text-align:right;left:120px;width:295px}
.value.right{left:783px;width:300px}

/* stats */
.stat{width:221px;height:210px;background:var(--navy);color:var(--white);text-align:center;padding-top:62px}
.stat b{display:block;font-size:38px;font-weight:400}
.stat span{display:block;font-size:16px;margin-top:12px}

/* footer */
.footer{left:0;top:3760px;width:1200px;height:421px;background:#000;color:var(--white)}
.fnav{left:567px;top:120px;display:flex;gap:26px;font-size:13px;font-weight:600}
.map{left:984px;top:117px;color:var(--gold);font-size:15px;text-decoration:underline}
.rule{left:114px;width:987px;height:1px;background:#333}
.contact{display:flex;gap:14px;align-items:flex-start}
.contact .ci{width:48px;height:48px;border-radius:50%;background:var(--gold);display:flex;align-items:center;justify-content:center;flex:none}
.contact small{display:block;font-size:11px;font-weight:500;margin:4px 0 6px}
.contact strong{display:block;font-size:19px;font-weight:600;line-height:26px}
.copy{left:0;top:378px;width:1200px;text-align:center;font-size:13px}
</style>
</head>
<body>

<!-- Hero -->
<section class="abs hero" role="img" aria-label="Cleaner vacuuming a bright office hallway, tinted navy"></section>
<div class="abs wordmark" style="left:140px;top:68px"><span class="wordmark-mark"></span>Harwood Cleaning</div>
<nav class="abs nav"><span class="active">HOME</span><span>ABOUT US</span><span>SERVICES</span><span>CONTACT US</span></nav>
<div class="abs call">
  <div class="call-icon"><svg width="20" height="20" viewBox="0 0 24 24" fill="#fff"><path d="M6.6 10.8a15 15 0 006.6 6.6l2.2-2.2a1 1 0 011-.25 11.4 11.4 0 003.6.6 1 1 0 011 1V20a1 1 0 01-1 1A17 17 0 013 4a1 1 0 011-1h3.5a1 1 0 011 1c0 1.25.2 2.45.6 3.6a1 1 0 01-.25 1z"/></svg></div>
  <div><small>CALL US TODAY</small><strong>0400 518 226</strong></div>
</div>
<h1 class="abs hero-title">30+ Years of <span>Commercial and<br>Residential Cleaning</span> in Sale</h1>
<p class="abs hero-sub">TRUSTED BY LOCALS FOR THREE DECADES</p>
<a class="abs btn btn-gold">GET A QUOTE</a>

<!-- Trust logos -->
<section class="abs trust">
  <div class="abs partner" style="left:143px"><span class="partner-mark"></span>RTB</div>
  <div class="abs partner" style="left:255px">Brightway</div>
  <div class="abs partner" style="left:420px">Eastvale District Health</div>
  <div class="abs partner" style="left:690px">KPL</div>
  <div class="abs reviews">
    <div class="row">4.5
      <svg width="128" height="20" viewBox="0 0 128 20" fill="var(--star)">
        <g id="s"><path d="M10 1l2.6 6 6.4.5-4.9 4.2 1.5 6.3L10 14.6 4.4 18l1.5-6.3L1 7.5l6.4-.5z"/></g>
        <use href="#s" x="27"/><use href="#s" x="54"/><use href="#s" x="81"/>
        <path d="M118 1l2.6 6 6.4.5-4.9 4.2 1.5 6.3-5.6-3.4-5.6 3.4 1.5-6.3-4.9-4.2 6.4-.5z" fill="none" stroke="var(--star)" stroke-width="1.5"/>
        <path d="M118 1v13.6l-5.6 3.4 1.5-6.3-4.9-4.2 6.4-.5z"/>
      </svg>
    </div>
    <div class="count">35 Rateline Reviews</div>
  </div>
</section>

<!-- Services -->
<h2 class="abs section-title" style="top:1078px">What <span>Our Services</span></h2>
<div class="abs" style="left:600px;top:1172px;width:1px;height:835px;background:#e4e4e4"></div>
<div class="abs" style="left:169px;top:1590px;width:431px;height:1px;background:#e4e4e4"></div>

<div class="photo" style="left:169px;top:1172px;background:linear-gradient(160deg,#2b2a30,#8a7a5a 45%,#c9d2dc 75%,#6f7a88)" role="img" aria-label="Floor polishing machine on a glossy commercial floor"></div>
<div class="svc-icon" style="left:486px;top:1402px"><svg width="34" height="34" viewBox="0 0 34 34" fill="none" stroke="#fff" stroke-width="2"><rect x="6" y="8" width="12" height="22"/><rect x="18" y="14" width="10" height="16"/><path d="M10 13h4M10 18h4M10 23h4M21 19h4M21 24h4"/></svg></div>
<div class="svc-text" style="left:169px;top:1460px"><h3>Commercial Cleaning</h3><p>Lorem ipsum dolor sit amet, consectetur adipiscing elit,<br>sed do eiusmod tempor incididunt ut</p></div>

<div class="photo" style="left:609px;top:1172px;background:linear-gradient(180deg,#c9cfd3 0%,#b88a3c 40%,#6f9a3a 70%,#8a3d2c 100%)" role="img" aria-label="Worker on a ladder cleaning house gutters"></div>
<div class="svc-icon" style="left:927px;top:1402px"><svg width="34" height="34" viewBox="0 0 34 34" fill="none" stroke="#fff" stroke-width="2"><path d="M5 16L17 6l12 10"/><path d="M8 14v15h18V14"/><rect x="14" y="19" width="6" height="10"/></svg></div>
<div class="svc-text" style="left:609px;top:1460px"><h3>Residential Cleaning</h3><p>Lorem ipsum dolor sit amet, consectetur adipiscing elit,<br>sed do eiusmod tempor incididunt ut</p></div>

<div class="card-raised"></div>
<div class="svc-text" style="left:169px;top:1622px"><h3>Window Cleaning</h3><p>Lorem ipsum dolor sit amet, consectetur adipiscing elit,<br>sed do eiusmod tempor incididunt ut</p></div>
<div class="photo" style="left:169px;top:1746px;background:linear-gradient(150deg,#1f3a63,#4f7fb0 50%,#c9dbe8 70%,#2c4e7a)" role="img" aria-label="Rope-access worker cleaning glass building facade"></div>
<div class="svc-icon" style="left:486px;top:1704px"><svg width="34" height="34" viewBox="0 0 34 34" fill="none" stroke="#fff" stroke-width="2"><rect x="7" y="5" width="20" height="24"/><path d="M7 12h20M17 12v17M4 29h26"/></svg></div>

<div class="svc-text" style="left:609px;top:1622px"><h3>Steam Cleaning</h3><p>Lorem ipsum dolor sit amet, consectetur adipiscing elit,<br>sed do eiusmod tempor incididunt ut</p></div>
<div class="photo" style="left:609px;top:1746px;background:linear-gradient(170deg,#5a6470,#cfd3d6 40%,#e6e6e6 60%,#4a4a4a)" role="img" aria-label="Steam cleaner releasing steam over carpet"></div>
<div class="svc-icon" style="left:927px;top:1704px"><svg width="34" height="34" viewBox="0 0 34 34" fill="none" stroke="#fff" stroke-width="2"><path d="M12 6c-2 3 2 5 0 8M17 4c-2 3 2 5 0 8M22 6c-2 3 2 5 0 8"/><path d="M6 18c0 6 5 11 11 11s11-5 11-11"/></svg></div>

<!-- Call to action band -->
<section class="abs cta" role="img" aria-label="Cleaner washing a brick wall, tinted gold">
  <h2>CALL THE CLEANERS YOU CAN COUNT ON</h2>
  <h4>WHEN YOU NEED HELP WITH CLEANING, THE LAST THING YOU WANT IS STRESS.</h4>
  <p>Too many people deal with the same problems cleaners not showing up, rushed work, or jobs left half-done.<br>You shouldn’t have to wonder whether the job will be done right.You deserve a team that turns up, does it properly,<br>and keeps things simple from start to finish.</p>
  <a class="abs btn btn-navy">LEARN MORE</a>
</section>

<!-- Core values -->
<h2 class="abs section-title" style="top:2803px">Our <span>Core Values</span></h2>
<div class="abs ring"></div>
<div class="abs ring-inner"></div>
<div class="abs wordmark" style="left:445px;top:3069px;width:310px;justify-content:center;color:var(--navy);font-size:24px">Harwood Cleaning</div>
<div class="abs dot" style="left:458px;top:2936px"></div>
<div class="abs dot" style="left:715px;top:2936px"></div>
<div class="abs dot" style="left:445px;top:3201px"></div>
<div class="abs dot" style="left:728px;top:3201px"></div>
<div class="abs value left" style="top:2903px"><h3>Make It Easy</h3><p>Lorem ipsum dolor sit amet, consectetur<br>adipiscing elit, sed do eius</p></div>
<div class="abs value right" style="top:2903px"><h3>Be Real</h3><p>Lorem ipsum dolor sit amet, consectetur<br>adipiscing elit, sed do eius</p></div>
<div class="abs value left" style="top:3186px"><h3>Have Fun</h3><p>Lorem ipsum dolor sit amet, consectetur<br>adipiscing elit, sed do eius</p></div>
<div class="abs value right" style="top:3186px"><h3>Do It Right</h3><p>Lorem ipsum dolor sit amet, consectetur<br>adipiscing elit, sed do eius</p></div>

<!-- Stats -->
<div class="abs stat" style="left:240px;top:3444px"><b>92+</b><span>Recurring Clients</span></div>
<div class="abs stat" style="left:490px;top:3444px"><b>4,150+</b><span>Visits Per Year</span></div>
<div class="abs stat" style="left:739px;top:3444px"><b>265+</b><span>Pre-Sale</span></div>

<!-- Footer -->
<footer class="abs footer">
  <div class="abs wordmark" style="left:133px;top:110px"><span class="wordmark-mark"></span>Harwood Cleaning</div>
  <nav class="abs fnav"><span>HOME</span><span>ABOUT US</span><span>SERVICES</span><span>CONTACT US</span></nav>
  <a class="abs map">View Map</a>
  <div class="abs rule" style="top:201px"></div>
  <div class="abs contact" style="left:133px;top:254px">
    <div class="ci"><svg width="18" height="22" viewBox="0 0 18 22" fill="#fff"><path d="M9 0a8 8 0 018 8c0 6-8 14-8 14S1 14 1 8a8 8 0 018-8zm0 5a3 3 0 100 6 3 3 0 000-6z"/></svg></div>
    <div><small>LOCATION</small><strong>18 Kinross Lane,<br>Marlow Bay VIC 3999</strong></div>
  </div>
  <div class="abs contact" style="left:472px;top:254px">
    <div class="ci"><svg width="22" height="16" viewBox="0 0 22 16" fill="#fff"><path d="M0 0h22v2L11 9 0 2z"/><path d="M0 4l11 7 11-7v12H0z"/></svg></div>
    <div><small>EMAIL US TODAY</small><strong>info@harwoodcleaning.example</strong></div>
  </div>
  <div class="abs contact" style="left:882px;top:254px">
    <div class="ci"><svg width="20" height="20" viewBox="0 0 24 24" fill="#fff"><path d="M6.6 10.8a15 15 0 006.6 6.6l2.2-2.2a1 1 0 011-.25 11.4 11.4 0 003.6.6 1 1 0 011 1V20a1 1 0 01-1 1A17 17 0 013 4a1 1 0 011-1h3.5a1 1 0 011 1c0 1.25.2 2.45.6 3.6a1 1 0 01-.25 1z"/></svg></div>
    <div><small>CALL US TODAY</small><strong>0400 518 226</strong></div>
  </div>
  <div class="abs rule" style="top:345px"></div>
  <p class="abs copy">Copyright@2025.All Rights Reserved</p>
</footer>

</body>
</html>
```